Yoga/movement guide/teacher for adult yoga practice and kid yoga

What is the positioning or mission statement of your company? to guide individuals in a yoga-based safe and sustainable movement practice applicable to all ages and body types. Currently my focus is working with children in daycare and school settings, but my goal is to expand into private yoga practice for adults, and potentially as part of rented space in studios. I hope to find a way to work with children AND adults (so would love for logo to be appealing to both), but current focus is with children based on need and demand in the community. yoga for children also compliments my backround as a pediatrician/neonatologist, and I greatly miss interacting with children. I also want to emphasize a yoga/movement practice that is focused more on what one feels internally through movement. NOT what one looks like asthetically. I believe in removing all mirrors from yoga/movement practice. It should be an experience of movement/poses/yoga through appropriate cueing and education. It is not about the details of how far the knee should bend, or how high the leg should be. Focusing on foudation first, core, then core engagement and ultimately expression of poses/movements. A focus on strength, stability and mobility, not just flexibility, which is the common perception/association with yoga. I also want individuals to learn to be an advocate of their own health. Through guidance, I hope for individuals to connect with their body so they know themselves so well to be able to advocate for themselves in the modern healthcare world. This internal experience and connection is so essential in a world where modern medicine has become a business and it is all about making a dollar. the connection with patients is lost, and individuals need to learn to empower themselves and through their new found voice to be able to articulate what is wrong.<br/>Does your company have a tagline or slogan that should be included with the logo? "Practice Glowing Motion"<br/>What do you hope your company can be known for? Accessible yoga for a sustained practice. A guided movement practice where one gains information and knowledge of oneself through a mind/body connection. For one feel good physically with a new awaraness of their internal radiance that exists in all beings. Physical rejuvenation egnites a light and increases energy to flow through the physical body, which ultimately tranlates into works of kindness for others and out in the world. <br/>What color palettes might you prefer? why? love the colors currently chosen<br/>Where will the logo be primarily used? initially business cards, but hopefully future websites, t-shirts, and potentially local magazine adds. Also starting with a small couple of banners for community events in the area. I currently practice as a nomad out of my car :)<br/>Are there any elements you would prefer to see in the logo? Movement. A modern depiction of a human body/figure practicing movement. Hoping to avoid a stereotypical yoga pose per say, just because I want to people to think of it more of a movement practice with yoga roots. Modern yoga. There are elements of breathing and connecting with oneself through the flow of breath and movement, but I do not focus on the meditative/cerebral aspect of the yoga practice. What I teach is almost reaching a meditative state through movement. I personally don't practice, nor resonate with just seated meditation. just not my thing :)<br/>In your opinion, what defines a well-designed logo? curiosity. enough info for individuals to think they know what it means, but want to know more. invokes curiosity, but not too abstract. Reproducible. not too complicated. I want also to invoke a community feel, so a design that appeals to all people within a community. <br/>What is your preference in reference to icons, typography, spokespeople (characters), etc.? modern design. I love the idea of a logo for my purposes, to invoke a sense of movement from within. So not too static. <br/>What words or icons must be included in the logo? movement with yoga roots. <br/>What logos do you like and why? A representation, but not exact. I think some ambiguity is intriguing for others, and also memorable. I want it to be an artistic representation of movement/yoga<br/>What logos do you dislike and why? too busy, too loud. <br/>In your opinion, what is the primary purpose for a logo? association<br/>Who is the primary target audience? (who is most likely to use your services/product?) Children and their parents, but ultimately to expand into teaching adults. I even have aspirations of prenatal and post-natal yoga. Potentially incorporating infants. <br/>Who currently uses your product the most? n/a (working in schools/daycare currently. It is currently all volunteer)<br/>Are you pleased with the range of people your company serves? n/a<br/>Are you looking to expand, modify, or completely change your target audience? or will it remain the same? yes! expand into an adult audience. <br/>How do you plan to focus on your target audience? currently by working through schools and daycares. hopefully ultimately through after school care programs and then offering kid yoga in an existing yoga studio (working on this with Q Loft in Ridgeland, currently)<br/>What are your main forms of advertising? word of mouth, schools, daycares. Happy kids talking to their parents about the yoga class they took and happy teachers :)<br/>How do most customers find out about your company?<br/>Which gender are you targeting? All genders! However, with kid yoga, often the maternal individual in the child's life is more involved with decision making as far as extracurricular activities

Target Market(s)

individuals and families interested in wellness and feeling great

Contact Information for Business Card

Dana Whitmore
Yoga Instructor
RYT-200, RCYT

certified yoga teacher for adults and children

Colors

Designer to choose colors to be used in the design.

Requirements
Must have
• "Practice Glowing Motion"
Nice to have
• logo with same colors

```html
<!DOCTYPE html>
<html lang="en">
<head>
<meta charset="utf-8">
<title>Brightway Studios – Business Card</title>
<link rel="stylesheet" href="https://fonts.googleapis.com/css2?family=Arimo:wght@400&family=Indie+Flower&family=Josefin+Sans:wght@300&display=swap">
<style>
  :root {
    --page: #2b2b2b;
    --card-grey: #858585;
    --band-grey: #7f7f7f;
    --paper: #ffffff;
    --sun: #f5db3c;
    --teal: #62c8d2;
    --ink: #6e6e6e;
    --light: #ffffff;
  }
  * { margin: 0; padding: 0; box-sizing: border-box; }
  html, body { width: 1200px; height: 900px; overflow: hidden; }
  body {
    background: var(--page);
    position: relative;
    font-family: "Arimo", Arial, sans-serif;
  }
  .card {
    position: absolute;
    width: 640px;
    height: 366px;
    overflow: hidden;
    box-shadow: 0 10px 30px rgba(0,0,0,.45);
  }
  .card--back { left: 420px; top: 50px; background: var(--card-grey); }
  .card--front { left: 140px; top: 480px; background: var(--paper); }

  .back-pattern {
    position: absolute; inset: 0;
    background: radial-gradient(ellipse at 60% 50%, #8d8d8d 0%, var(--card-grey) 70%);
  }
  .back-mark {
    position: absolute; left: 50%; top: 50%;
    transform: translate(-50%, -50%);
    display: flex; align-items: center; gap: 14px;
    font-family: "Josefin Sans", sans-serif; font-weight: 300;
    font-size: 40px; color: var(--sun); letter-spacing: 1px;
  }
  .mark-dot { width: 34px; height: 34px; border-radius: 50%; background: var(--sun); flex: none; }

  .brand { position: absolute; left: 34px; top: 58px; }
  .brand__name {
    display: flex; align-items: center; gap: 12px;
    font-family: "Josefin Sans", sans-serif; font-weight: 300;
    font-size: 36px; color: var(--ink);
  }
  .brand__dot { width: 40px; height: 40px; border-radius: 50%; background: var(--sun); flex: none; }
  .brand__tagline {
    margin: 8px 0 0 52px;
    font-family: "Josefin Sans", sans-serif; font-weight: 300;
    font-size: 10px; letter-spacing: 2px; text-transform: uppercase; color: var(--teal);
  }

  .wave { position: absolute; left: 0; top: 0; width: 640px; height: 366px; }

  .contact {
    position: absolute; right: 30px; top: 206px; text-align: right; color: var(--light);
  }
  .contact__name {
    font-family: "Indie Flower", cursive; font-size: 32px; color: var(--sun); line-height: 1;
  }
  .contact__role { font-size: 17px; margin-top: 2px; }
  .contact__list { list-style: none; margin-top: 14px; font-size: 16px; line-height: 24px; }
  .contact__list li { display: flex; justify-content: flex-end; align-items: center; gap: 10px; }
  .contact__list svg { width: 16px; height: 16px; flex: none; }
</style>
</head>
<body>

<section class="card card--back">
  <div class="back-pattern" role="img" aria-label="Faint tone-on-tone spiral pattern across the card back"></div>
  <div class="back-mark"><span class="mark-dot"></span>Brightway</div>
</section>

<section class="card card--front">
  <div class="brand">
    <div class="brand__name"><span class="brand__dot"></span>Brightway Studios</div>
    <p class="brand__tagline">Practice Glowing Motion</p>
  </div>

  <svg class="wave" viewBox="0 0 640 366" aria-hidden="true">
    <path d="M0,318 C110,306 220,282 330,230 C230,290 110,326 0,338 Z" fill="var(--sun)"/>
    <path d="M0,344 C180,320 330,150 480,148 C560,147 610,160 640,170 L640,366 L0,366 Z" fill="var(--teal)"/>
    <path d="M0,352 C180,332 330,166 480,165 C560,164 610,178 640,190 L640,366 L0,366 Z" fill="var(--band-grey)"/>
  </svg>

  <div class="contact">
    <p class="contact__name">Dana Whitmore</p>
    <p class="contact__role">Owner-Operator</p>
    <ul class="contact__list">
      <li>555-014-2290
        <svg viewBox="0 0 16 16"><circle cx="8" cy="8" r="7" fill="none" stroke="var(--teal)" stroke-width="1.3"/><path d="M5.5,4.5 L7,6.5 L6.3,7.4 C6.8,8.5 7.6,9.3 8.6,9.8 L9.5,9.1 L11.5,10.5 L10.6,11.6 C7.8,11.4 4.6,8.2 4.4,5.4 Z" fill="var(--teal)"/></svg>
      </li>
      <li>danawhitmore@mailbox.com
        <svg viewBox="0 0 16 16"><rect x="1.5" y="3.5" width="13" height="9" fill="none" stroke="var(--teal)" stroke-width="1.3"/><path d="M1.5,3.5 L8,9 L14.5,3.5" fill="none" stroke="var(--teal)" stroke-width="1.3"/></svg>
      </li>
      <li>www.brightwaystudios.com
        <svg viewBox="0 0 16 16"><circle cx="8" cy="8" r="7" fill="var(--teal)"/><path d="M1,8 H15 M8,1 C4,4 4,12 8,15 M8,1 C12,4 12,12 8,15" fill="none" stroke="var(--band-grey)" stroke-width="1"/></svg>
      </li>
    </ul>
  </div>
</section>

</body>
</html>
```